Exciting business card design for diesel performance and offroad business!!

We need a business card design that looks good and stands out. I don't want a plain old boring business card that you forget about and throw away at the end of the day. We are a diesel performance and truck accessory business that sell and install the industries biggest brands and best parts out there!

Industry/Entity Type

Business

Contact Information for Business Card

Dalton Prewick (Owner) 260-587-3146
bramble.motorworks@postmoor.com
Truck and Off-Road Performance and Accessories

Requirements
Must have
• A great look and feel about it. My logo needs to be in center of the card just like the attached picture. On the back I want it to have a list of items we offer
• Truck and Rovex: Lift and Leveling Kits, Intake and Exhaust Systems, Custom Tuning, Wheels and Tires, Steps, Bed Covers, Floor Liners, Custom Lighting, Turbos and Piping, Gauges, Much More!
• UTV: Suspension, Roll Cage, Doors, Exhaust, Tuning, Turbo Kits, Stereo, Wheels/Tires, Custom Lighting, Clutching, Much More!!

```html
<!DOCTYPE html>
<html lang="en">
<head>
<meta charset="utf-8">
<title>Bramble Motorworks LLC – Business Card</title>
<link href="https://fonts.googleapis.com/css2?family=Orbitron:wght@400;500;700&display=swap" rel="stylesheet">
<style>
  :root {
    --page: #1c1c1e;
    --ink-black: #0b0b0c;
    --asphalt-1: #2e2e2f;
    --asphalt-2: #121213;
    --steel-1: #5d6166;
    --steel-2: #a4a9ae;
    --steel-3: #3f4246;
    --text-light: #f2f2f2;
    --text-muted: #9a9a9a;
    --rule: #1a1a1a;
  }
  * { box-sizing: border-box; margin: 0; padding: 0; }
  html, body { width: 1200px; height: 800px; overflow: hidden; }
  body {
    background: var(--page);
    font-family: "Orbitron", sans-serif;
    color: var(--text-light);
    display: flex;
    align-items: center;
    justify-content: center;
    gap: 40px;
  }
  .card {
    width: 540px;
    height: 309px;
    position: relative;
    overflow: hidden;
    border-radius: 3px;
  }

  /* Front */
  .card-front {
    background: radial-gradient(ellipse at 50% 45%, var(--asphalt-1) 0%, var(--asphalt-2) 75%, var(--ink-black) 100%);
    display: flex;
    align-items: center;
    justify-content: center;
  }
  .brand {
    display: flex;
    flex-direction: column;
    align-items: center;
    gap: 16px;
    text-align: center;
  }
  .brand-mark {
    width: 96px;
    height: 96px;
    border-radius: 50%;
    background: var(--steel-2);
  }
  .brand-name {
    font-size: 22px;
    line-height: 30px;
    font-weight: 700;
    letter-spacing: 3px;
    text-transform: uppercase;
    color: var(--text-light);
    width: 320px;
  }

  /* Back */
  .card-back {
    background: linear-gradient(115deg, var(--steel-3) 0%, var(--steel-1) 30%, var(--steel-2) 48%, var(--steel-1) 62%, var(--steel-3) 100%);
  }
  .service-list {
    position: absolute;
    list-style: none;
    font-size: 11.5px;
    line-height: 15px;
    font-weight: 400;
  }
  .service-list .list-heading {
    font-size: 13px;
    font-weight: 500;
    margin-bottom: 3px;
    padding-left: 0;
  }
  .service-list li { padding-left: 14px; position: relative; }
  .service-list li:not(.list-heading)::before {
    content: "";
    position: absolute;
    left: 2px;
    top: 4px;
    width: 7px;
    height: 7px;
    border-radius: 50%;
    background: var(--ink-black);
    border: 1.5px solid var(--text-light);
  }
  .list-truck { left: 22px; top: 14px; }
  .list-utv { left: 300px; top: 26px; }
  .tagline {
    position: absolute;
    left: 96px;
    top: 220px;
    font-size: 10.5px;
    color: var(--ink-black);
    font-weight: 500;
  }
  .contact-band {
    position: absolute;
    left: 0; right: 0; bottom: 0;
    height: 70px;
    background: var(--ink-black);
    border-top: 2px solid var(--rule);
  }
  .owner { position: absolute; left: 22px; top: 14px; }
  .owner-name { font-size: 17px; font-weight: 500; letter-spacing: 1px; text-transform: uppercase; }
  .owner-role { font-size: 11px; color: var(--text-muted); text-transform: uppercase; margin-top: 3px; }
  .contact { position: absolute; right: 22px; top: 10px; text-align: right; }
  .contact-phone { font-size: 26px; font-weight: 500; letter-spacing: 1px; }
  .contact-email { font-size: 11px; margin-top: 4px; color: var(--text-light); }
</style>
</head>
<body>
  <section class="card card-front" aria-label="Card front">
    <div class="brand">
      <span class="brand-mark"></span>
      <span class="brand-name">Bramble Motorworks LLC</span>
    </div>
  </section>

  <section class="card card-back" aria-label="Card back">
    <ul class="service-list list-truck">
      <li class="list-heading">TRUCK AND ROVEX</li>
      <li>Lift and Leveling Kits</li>
      <li>Intake and Exhaust Systems</li>
      <li>Custom Tuning</li>
      <li>Wheels and Tires</li>
      <li>Steps</li>
      <li>Bed Covers</li>
      <li>Floor Liners</li>
      <li>Custom Lighting</li>
      <li>Turbos and Piping</li>
      <li>Gauges</li>
      <li>Much More!</li>
    </ul>
    <ul class="service-list list-utv">
      <li class="list-heading">UTV</li>
      <li>Suspension</li>
      <li>Roll Cage</li>
      <li>Doors</li>
      <li>Exhaust</li>
      <li>Tuning</li>
      <li>Turbo Kits</li>
      <li>Stereo</li>
      <li>Wheels/Tires</li>
      <li>Custom Lighting</li>
      <li>Clutching</li>
      <li>Much More!!</li>
    </ul>
    <p class="tagline">Truck and offroad performance and Accessories</p>
    <div class="contact-band">
      <div class="owner">
        <p class="owner-name">Dalton Prewick</p>
        <p class="owner-role">Owner</p>
      </div>
      <div class="contact">
        <p class="contact-phone">260-587-3146</p>
        <p class="contact-email">bramble.motorworks@postmoor.com</p>
      </div>
    </div>
  </section>
</body>
</html>
```